Financial Services Consultant Marketing Brochure

I need a marketing brochure for a financial services consulting firm that focuses on internal audit, risk management, and regulatory management. I ma a new company and am trying to make a good first impression. The brochure needs to point out my mission, target market, and products.

Target Market(s)

Financial Services companies, small to midsize banks.

Industry/Entity Type

Financial Service

Colors
ffc214
fece3e
fee18a
fcca95
faa54b
f78f20
f37122
f68e4e
f9bb94

Requirements
Must have
• Needs to be conservative, but impactful. Must use my existing logo. Must incorporate the information that is in the enclosed strategy document.
• Must be in a tri-fold format
• Address should be:
• 418 Welden Street
• 9th Floor
• New York, NY 10284
Nice to have
• Pictures of people interacting.
Should not have
• Any $ or references to money.

```html
<!DOCTYPE html>
<html lang="en">
<head>
<meta charset="utf-8">
<title>Keston Assurance Advisors – Tri-fold Brochure</title>
<link rel="stylesheet" href="https://fonts.googleapis.com/css2?family=Lato:wght@300;400;700&family=Oswald:wght@500&display=swap">
<style>
  :root {
    --gold: #e3ab2c;
    --grey-band: #8e8e94;
    --ink: #3e3e44;
    --text: #4a4a50;
    --paper: #ffffff;
    --backdrop: #6c6c77;
    --photo-a: #c9ccd3;
    --photo-b: #7f8593;
  }
  * { box-sizing: border-box; margin: 0; padding: 0; }
  html, body { width: 1200px; height: 1200px; overflow: hidden; }
  body {
    background: var(--backdrop);
    font-family: "Lato", sans-serif;
    color: var(--text);
    position: relative;
  }
  .spread {
    position: absolute; left: 82px; top: 200px;
    width: 1035px; height: 800px;
    display: flex; background: var(--paper);
  }
  .panel { position: relative; width: 345px; height: 800px; overflow: hidden; }
  .panel + .panel { border-left: 1px solid #e6e6ea; }

  .label {
    display: inline-flex; align-items: center; gap: 6px;
    background: var(--grey-band); color: #fff;
    font-size: 10px; font-weight: 700;
    padding: 2px 12px 2px 20px; border-radius: 0 10px 10px 0;
    margin-left: -20px;
  }
  .label .dot {
    width: 18px; height: 18px; border-radius: 50%;
    background: #fff; border: 2px solid var(--gold);
  }
  .copy { font-size: 8.3px; line-height: 1.38; text-align: justify; margin: 10px 0 18px; }

  .info-panel { padding: 30px 22px 0 22px; }
  .info-panel .copy { font-size: 8px; }

  .products-panel { padding: 40px 22px 0 22px; }
  .products-panel .copy { font-size: 8.6px; line-height: 1.3; }

  /* brand name: one colour, one weight, one plain circle */
  .brand { display: flex; align-items: center; gap: 10px; }
  .brand-mark { width: 14px; height: 14px; border-radius: 50%; background: var(--gold); flex: none; }
  .brand-name {
    font-family: "Lato", sans-serif; font-weight: 400;
    font-size: 30px; letter-spacing: 3px; color: var(--gold);
  }

  .contact { text-align: center; margin-top: 50px; color: var(--ink); }
  .contact .brand { justify-content: center; margin-bottom: 30px; }
  .contact svg { display: block; margin: 0 auto 4px; }
  .contact p { font-size: 12px; margin-bottom: 14px; }
  .contact .phone { font-size: 16px; }

  .bands { position: absolute; left: 0; top: 0; }

  .cover-panel .brand { position: absolute; top: 44px; left: 30px; }
  .tagline { position: absolute; left: 44px; top: 690px; transform: rotate(-8deg); transform-origin: left top; }
  .tagline .lead { font-size: 22px; font-weight: 400; color: var(--ink); }
  .tagline .service { font-family: "Oswald", sans-serif; font-size: 19px; color: var(--gold); letter-spacing: .3px; }
  .tagline .url { font-size: 9px; letter-spacing: 2px; color: #555; margin-top: 12px; padding-left: 22px; }
</style>
</head>
<body>
<main class="spread">

  <section class="panel info-panel">
    <span class="label"><span class="dot"></span>Mission Statement</span>
    <p class="copy">Keston Assurance Advisors' (KESTON) purpose is to provide audit, risk, and regulatory expertise to financial services companies throughout the United States. Using ethics and integrity as our cornerstones and competency as our capstone, KESTON provides consulting services that will ensure that our clients and the financial services industry remain viable, safe, and solvent. KESTON strives to ensure our client's internal audit departments are risk-based and add value, risk management practices and processes are appropriate for their risk profiles, and clients have the ability to manage the regulatory environment, adapt to regulatory changes, and remain compliant with all regulations.</p>
    <span class="label"><span class="dot"></span>Vision</span>
    <p class="copy">KESTON will provide consulting services in three basic categories; Internal Audit, Risk Management, and Regulatory Environment. Internal Audit will be KESTON's primary focus and will serve as its core service. Nonetheless, KESTON has the expertise and capacity to offer products in Risk Management and the Regulatory Environment.</p>
    <span class="label"><span class="dot"></span>Markets</span>
    <p class="copy">KESTON's primary area of operation will be in the Mid-Atlantic and Northeast states. However, KESTON has the capacity to take assignments in any state in the continental United States. KESTON's resource plan is to use, to the extent possible, local talent enabling the engagements to remain connected to the client's location and reduce associated travel costs.</p>
    <p class="copy">KESTON's primary client base will be small and midsize community banks, credit unions, and the foreign branch operations of international banks. These banks will typically operate in the retail and/or commercial sector. KESTON will accept engagements at larger banks; however, initially KESTON will only focus on risk management activities associated with commercial and retail type of banking activities in these larger institutions.</p>
  </section>

  <section class="panel products-panel">
    <span class="label"><span class="dot"></span>Products</span>
    <p class="copy">The core product and services will be in Internal Audit, while Risk Management and Regulatory product and services will be used to supplement the core products. All audits conducted or participated in by KESTON will be conducted in accordance with the Guild of Internal Reviewers (GIR) Core Review Practices Framework (CRPF), generally referred to as the "Standards".</p>
    <div class="contact">
      <div class="brand"><span class="brand-mark"></span><span class="brand-name">KESTON</span></div>
      <svg width="14" height="14" viewBox="0 0 24 24"><path fill="var(--gold)" d="M6.6 10.8a15.1 15.1 0 006.6 6.6l2.2-2.2a1 1 0 011-.25 11.4 11.4 0 003.6.57 1 1 0 011 1V20a1 1 0 01-1 1A17 17 0 013 4a1 1 0 011-1h3.5a1 1 0 011 1c0 1.25.2 2.45.57 3.57a1 1 0 01-.25 1z"/></svg>
      <p class="phone">212-555-0148</p>
      <svg width="14" height="10" viewBox="0 0 24 16"><rect x="1" y="1" width="22" height="14" fill="none" stroke="var(--gold)" stroke-width="1.5"/><path d="M1 1l11 8 11-8" fill="none" stroke="var(--gold)" stroke-width="1.5"/></svg>
      <p>hello@kestonadvisors.com</p>
      <svg width="14" height="14" viewBox="0 0 24 24" fill="none" stroke="var(--gold)" stroke-width="1.5"><circle cx="12" cy="12" r="10"/><ellipse cx="12" cy="12" rx="4.5" ry="10"/><path d="M2 12h20M4 6.5h16M4 17.5h16"/></svg>
      <p>www.kestonadvisors.com</p>
      <svg width="12" height="16" viewBox="0 0 24 32"><path fill="var(--gold)" d="M12 0a11 11 0 00-11 11c0 8 11 21 11 21s11-13 11-21A11 11 0 0012 0zm0 16a5 5 0 110-10 5 5 0 010 10z"/></svg>
      <p>418 Welden Street<br>New York, NY 10284</p>
    </div>
  </section>

  <section class="panel cover-panel">
    <svg class="bands" width="345" height="800" viewBox="0 0 345 800">
      <defs>
        <linearGradient id="coverPhoto" x1="0" y1="0" x2="1" y2="1">
          <stop offset="0" stop-color="var(--photo-a)"/>
          <stop offset="1" stop-color="var(--photo-b)"/>
        </linearGradient>
      </defs>
      <polygon points="0,168 345,83 345,103 0,188" fill="var(--grey-band)"/>
      <polygon points="0,156 345,71 345,85 0,170" fill="var(--gold)"/>
      <polygon points="0,188 345,103 345,565 0,650" fill="url(#coverPhoto)" role="img" aria-label="Photo of smiling business team in suits"/>
      <polygon points="0,650 345,565 345,580 0,665" fill="var(--gold)"/>
      <polygon points="0,665 345,580 345,590 0,675" fill="var(--grey-band)"/>
    </svg>
    <div class="brand"><span class="brand-mark"></span><span class="brand-name">KESTON</span></div>
    <div class="tagline">
      <div class="lead">KESTON will provide</div>
      <div class="service">CONSULTING SERVICES</div>
      <div class="url">www.kestonadvisors.com</div>
    </div>
  </section>

  <svg class="bands" width="690" height="800" viewBox="0 0 690 800">
    <defs>
      <linearGradient id="deskPhoto" x1="0" y1="0" x2="1" y2="1">
        <stop offset="0" stop-color="#d6d7db"/>
        <stop offset="1" stop-color="#f2f2f4"/>
      </linearGradient>
    </defs>
    <polygon points="0,692 345,632 690,700 690,800 0,800" fill="url(#deskPhoto)" role="img" aria-label="Greyscale photo of a hand writing over business charts"/>
    <polyline points="0,684 345,624 690,692" fill="none" stroke="var(--gold)" stroke-width="9"/>
  </svg>
</main>
</body>
</html>
```